Amber Orchard (instructional dating book)

Title: Amber Orchard
Subtitle: Where to plant tulips along a crooked brick path
Author: R.K. Tolvane
I'm seeking the title to be central with the subtitle underneath and the author slightly lower and to the left. Perhaps a border or two around the font. I thought the background could look aged (off color and old textured paper) and the background slightly punched into the texture like a typewriter has been used. I imagine it something like an old Pemberworth playbook or 1940s morse code manual. Many thanks!

Target Market(s)

18 to 45 year old single people

Industry/Entity Type

Dating

Font styles to use
Serif

Requirements
Must have
• Text with border or two
Nice to have
• Traditional feel. The book is instructional.
Should not have
• Too much color or flair

```html
<!DOCTYPE html>
<html lang="en">
<head>
<meta charset="utf-8">
<title>Amber Orchard — R.K. Tolvane</title>
<link rel="stylesheet" href="https://fonts.googleapis.com/css2?family=Cinzel:wght@400;500&family=Cormorant+Garamond:ital,wght@1,500&display=swap">
<style>
  :root {
    --paper: #e7cea5;
    --paper-light: #eed9b5;
    --paper-dark: #dcc093;
    --ink: #1e1914;
    --ink-faint: rgba(30, 25, 20, 0.16);
  }
  * { margin: 0; padding: 0; box-sizing: border-box; }
  html, body { width: 950px; height: 1200px; overflow: hidden; background: var(--paper); }
  .cover {
    position: relative;
    width: 950px;
    height: 1200px;
    overflow: hidden;
    color: var(--ink);
    background:
      radial-gradient(ellipse at 50% 45%, var(--paper-light) 0%, var(--paper) 55%, var(--paper-dark) 100%);
  }
  .corner-ornament {
    position: absolute;
    width: 224px;
    height: 224px;
    background: var(--ink-faint);
    border-radius: 40px;
  }
  .corner-ornament.top-left { left: 28px; top: 28px; }
  .corner-ornament.top-right { right: 28px; top: 28px; }
  .corner-ornament.bottom-left { left: 28px; bottom: 28px; }
  .corner-ornament.bottom-right { right: 28px; bottom: 28px; }

  .flourish-rule {
    position: absolute;
    left: 328px;
    width: 300px;
    height: 10px;
    background: var(--ink-faint);
    border-radius: 5px;
  }
  .flourish-rule.top { top: 38px; }
  .flourish-rule.bottom { top: 1154px; }

  .side-rule {
    position: absolute;
    top: 316px;
    width: 1px;
    height: 572px;
    background: var(--ink);
  }
  .side-rule.left { left: 41px; }
  .side-rule.right { left: 900px; }
  .side-ornament {
    position: absolute;
    top: 496px;
    width: 16px;
    height: 200px;
    background: var(--ink-faint);
    border-radius: 8px;
  }
  .side-ornament.left { left: 33px; }
  .side-ornament.right { left: 892px; }

  .author {
    position: absolute;
    top: 150px;
    left: 0;
    width: 928px;
    text-align: center;
    font-family: "Cinzel", serif;
    font-weight: 400;
    font-size: 36px;
    letter-spacing: 2px;
  }

  .title-frame {
    position: absolute;
    left: 0;
    top: 0;
    width: 950px;
    height: 600px;
  }
  .heart-mark {
    position: absolute;
    left: 404px;
    top: 314px;
    width: 128px;
    height: 124px;
    background: var(--ink-faint);
    border-radius: 50% 50% 50% 50% / 40% 40% 60% 60%;
  }
  .title {
    position: absolute;
    top: 442px;
    left: 0;
    width: 936px;
    text-align: center;
    font-family: "Cinzel", serif;
    font-weight: 400;
    font-size: 50px;
    letter-spacing: 1px;
    line-height: 1;
    white-space: nowrap;
  }
  .title .cap { font-size: 70px; }
  .subtitle {
    position: absolute;
    top: 572px;
    left: 0;
    width: 928px;
    text-align: center;
    font-family: "Cormorant Garamond", serif;
    font-style: italic;
    font-weight: 500;
    font-size: 34px;
    line-height: 66px;
  }
</style>
</head>
<body>
  <main class="cover">
    <div class="corner-ornament top-left" role="img" aria-label="Ornamental scroll and leaf corner piece"></div>
    <div class="corner-ornament top-right" role="img" aria-label="Ornamental scroll and leaf corner piece"></div>
    <div class="corner-ornament bottom-left" role="img" aria-label="Ornamental scroll and leaf corner piece"></div>
    <div class="corner-ornament bottom-right" role="img" aria-label="Ornamental scroll and leaf corner piece"></div>

    <div class="flourish-rule top" role="img" aria-label="Decorative flourish rule"></div>
    <div class="flourish-rule bottom" role="img" aria-label="Decorative flourish rule"></div>

    <div class="side-rule left"></div>
    <div class="side-rule right"></div>
    <div class="side-ornament left" role="img" aria-label="Decorative vertical flourish"></div>
    <div class="side-ornament right" role="img" aria-label="Decorative vertical flourish"></div>

    <p class="author">R.K. TOLVANE</p>

    <svg class="title-frame" width="950" height="600" viewBox="0 0 950 600" aria-hidden="true">
      <path d="M164 423 H354 V400 A114 126 0 0 1 582 400 V423 H770" fill="none" stroke="#1e1914" stroke-width="3"/>
      <line x1="234" y1="540" x2="708" y2="540" stroke="#1e1914" stroke-width="3"/>
    </svg>
    <div class="heart-mark" role="img" aria-label="Calligraphic scrolled heart emblem"></div>

    <h1 class="title"><span class="cap">A</span>MBER <span class="cap">O</span>RCHARD</h1>

    <p class="subtitle">Where to plant tulips along<br>a crooked brick path</p>
  </main>
</body>
</html>
```